Thai Restruant Business Card Design

A Business card design for a Thai and Laos take away restaurant.

We are a highly respectable take away restaurant in a small shopping center.

The design must have a Papaya Tree and Thai Palace.

The final design should communicate, innovation, fun and delicious food.

Industry/Entity Type

Restaurant

Contact Information for Business Card

Mango Hearth, Thai & Lao Kitchen, Shop 4. 17 Elmsworth Lane. Linfield N.S.W 2931, Tel. 02-96417725, Open 7 Days From 9.00am To 7.00pm

```html
<!DOCTYPE html>
<html lang="en">
<head>
<meta charset="utf-8">
<title>Mango Hearth – Business Card</title>
<link href="https://fonts.googleapis.com/css2?family=Baloo+2:wght@700;800&display=swap" rel="stylesheet">
<style>
  :root {
    --page-bg: #f2f2f2;
    --card-green: #a9c50f;
    --swoosh-olive: #8c8a1c;
    --text-red: #b3121f;
    --photo-light: #ffd36a;
    --photo-mid: #f7a21b;
    --photo-deep: #e8741c;
    --plate-red: #a8141c;
  }
  * { margin: 0; padding: 0; box-sizing: border-box; }
  html, body {
    width: 1200px;
    height: 768px;
    overflow: hidden;
    background: var(--page-bg);
  }
  .business-card {
    position: absolute;
    left: 100px;
    top: 79px;
    width: 1000px;
    height: 610px;
    background: var(--card-green);
    overflow: hidden;
    box-shadow: 0 6px 18px rgba(0,0,0,0.18);
    font-family: "Baloo 2", "Trebuchet MS", sans-serif;
    color: var(--text-red);
  }
  .card-art {
    position: absolute;
    inset: 0;
    width: 100%;
    height: 100%;
  }
  .card-text {
    position: absolute;
    left: 62px;
    top: 150px;
  }
  .brand-name,
  .cuisine {
    font-size: 46px;
    font-weight: 800;
    line-height: 1.0;
    display: block;
  }
  .address {
    margin-top: 72px;
    font-size: 24px;
    font-weight: 700;
    line-height: 1.15;
  }
  .phone {
    margin-top: 58px;
    margin-left: 20px;
    font-size: 30px;
    font-weight: 700;
  }
  .hours {
    margin-top: 30px;
    margin-left: 44px;
    font-size: 30px;
    font-weight: 700;
    white-space: nowrap;
  }
</style>
</head>
<body>
  <div class="business-card">
    <svg class="card-art" viewBox="0 0 1000 610" preserveAspectRatio="none">
      <defs>
        <linearGradient id="dish-tones" x1="0" y1="0" x2="1" y2="1">
          <stop offset="0" stop-color="var(--photo-light)"/>
          <stop offset="0.45" stop-color="var(--photo-mid)"/>
          <stop offset="0.8" stop-color="var(--photo-deep)"/>
          <stop offset="1" stop-color="var(--plate-red)"/>
        </linearGradient>
      </defs>
      <path class="swoosh-band" fill="var(--swoosh-olive)"
            d="M1000 0 L1000 10 C720 50 440 190 440 330 C440 470 700 545 1000 565 L1000 590 C660 575 415 480 418 330 C421 170 720 30 1000 0 Z"/>
      <path class="dish-photo" role="img" aria-label="Photo of halved papayas topped with nuts on a white plate"
            fill="url(#dish-tones)"
            d="M1000 10 C720 50 460 190 460 330 C460 470 700 545 1000 565 Z"/>
    </svg>

    <div class="card-text">
      <h1 class="brand-name">Mango Hearth</h1>
      <span class="cuisine">Thai &amp; Lao Kitchen</span>
      <p class="address">Shop 4. 17 Elmsworth Lane<br>Linfield N.S.W 2931</p>
      <p class="phone">Tel. 02-96417725</p>
      <p class="hours">Open 7 Days From 9.00am To 7.00pm</p>
    </div>
  </div>
</body>
</html>
```